Larkspur Homes - wanted BRILLIANT website design for our new property investing company

We need a website design for our new company based in Bristol, England, UK called "Larkspur Homes". We help buy people property who are in financial difficulty or who are needing to sell their property quickly for reasons such as death, divorce/separation, relocation, emigration.

We have a logo being designed incorporating strawberry and property (so red and green). We would like designs to communicate an elegant ,professional, approachable, friendly
fresh clean but also warm appealing appearance
Not too busy
Website consistent with logo and company name i.e. colour scheme

Please use our word document for content as a guide but use professional judgement for minor alterations if you feel they would benefit the site/structure etc

Please ask at any time if not sure

Target Market(s)

Adult british population, those that have a mortgage / loan / own property

Industry/Entity Type

Financial

Font styles to use
Serif
Sans Serif
Decorative

Colors
0692cd
33b7a4
acd036
fbee3e
3176b5
886aae
a6479a
e567a6
eb1f27

Requirements
Must have
• This must not look like a template website we are looking for UNIQUE please!
Nice to have
• Bristol pictures instead of generic, or colourful line drawings/comic drawings of houses/property/keys/happy people.....
Should not have
• An obvious off the shelf template design

```html
<!DOCTYPE html>
<html lang="en">
<head>
<meta charset="utf-8">
<title>Larkspur Homes</title>
<link href="https://fonts.googleapis.com/css2?family=Open+Sans:wght@400;600;700&display=swap" rel="stylesheet">
<style>
:root{
  --red:#e8141b;
  --green:#00c257;
  --dark:#2a2c2c;
  --darker:#1b1b1b;
  --grey-band:#e8e8e8;
  --text:#444;
  --muted:#9a9a9a;
  --footer-text:#cfcfcf;
  --navy:#12306b;
}
*{box-sizing:border-box;margin:0;padding:0}
html,body{width:834px;height:1200px;overflow:hidden}
body{position:relative;font-family:'Open Sans',Arial,sans-serif;color:var(--text);background:#fff}
.abs{position:absolute}

/* header */
.site-header{position:absolute;left:0;top:0;width:834px;height:66px;background:var(--dark)}
.brand{position:absolute;left:138px;top:20px;font-size:21px;color:var(--red);font-weight:400;letter-spacing:.2px}
.header-contact{position:absolute;right:138px;top:24px;text-align:right;font-size:8.5px;line-height:12px;color:#bbb}
.header-contact svg{vertical-align:-1px;margin-right:3px}

/* nav */
.main-nav{position:absolute;left:0;top:66px;width:834px;height:26px;background:var(--green);border-bottom:1px solid #0a9d49}
.main-nav a{position:absolute;top:0;height:26px;line-height:26px;color:#fff;font-size:10.5px;font-weight:600;text-align:center;text-decoration:none;border-right:1px solid #17a955}
.main-nav a.active{background:var(--red);border-right:none}

/* hero */
.hero{position:absolute;left:0;top:92px;width:834px;height:275px}
.hero-photo{position:absolute;inset:0;background:linear-gradient(90deg,#6c6a66 0%,#d8d8d6 25%,#e9ecec 45%,#c6c9c2 60%,#5b4e45 80%,#7a6a5e 100%)}
.hero-photo::after{content:"";position:absolute;inset:0;background:linear-gradient(180deg,rgba(255,255,255,.15) 0%,rgba(255,255,255,0) 50%,rgba(30,30,30,.35) 100%)}
.hero-title{position:absolute;left:0;width:834px;top:58px;text-align:center;font-size:29px;line-height:33px;color:#333;font-weight:400}
.hero-btn{position:absolute;left:376px;top:144px;width:82px;height:34px;background:var(--red);color:#fff;font-size:20px;font-weight:600;text-align:center;line-height:34px}
.hero-dots{position:absolute;left:400px;top:238px;display:flex;gap:3px}
.hero-dots span{width:9px;height:9px;border-radius:50%;border:1.5px solid #fff;background:rgba(0,0,0,.3)}
.hero-dots span.on{background:var(--green)}

/* intro */
.section-title{color:var(--red);font-weight:600}
.intro-title{position:absolute;left:140px;top:400px;width:340px;font-size:14px;line-height:18px}
.intro-figure{position:absolute;left:140px;top:442px;width:72px;height:163px;background:linear-gradient(180deg,#e4d2c4 0%,#2b2b2e 14%,#1f1f22 80%,#111 100%);border-radius:30px 30px 6px 6px}
.service-list{position:absolute;left:227px;top:453px;width:265px;list-style:none;font-size:10px;line-height:15.4px;color:#555}

.form-title{position:absolute;left:501px;top:401px;font-size:14px}
.contact-form{position:absolute;left:501px;top:432px;width:196px;height:197px;background:#f7f7f7;border:1px solid #ececec}
.field{position:absolute;left:11px;width:174px;height:20px;background:#fff;border:1px solid #e6e6e6;font-size:7px;font-style:italic;color:#aaa;padding:5px 10px}
.send-btn{position:absolute;left:65px;top:166px;width:65px;height:20px;background:var(--green);color:#fff;font-size:11px;font-weight:600;text-align:center;line-height:20px}

/* help */
.help{position:absolute;left:0;top:646px;width:834px;height:223px;background:var(--grey-band)}
.help-title{position:absolute;left:0;width:834px;top:30px;text-align:center;font-size:16px}
.help-item{position:absolute;font-size:10px;color:#333;font-weight:500;height:14px;line-height:14px;padding-left:22px}
.help-item b{position:absolute;left:0;top:1px;width:12px;height:12px;border-radius:50%;background:var(--green);color:#fff;font-size:6.5px;line-height:12px;text-align:center;font-weight:700}

/* partners */
.partners-title{position:absolute;left:0;width:834px;top:890px;text-align:center;font-size:16px}
.partner-badge{position:absolute;top:943px;height:34px}

/* footer */
.site-footer{position:absolute;left:0;top:1010px;width:834px;height:170px;background:var(--dark);color:var(--footer-text)}
.footer-brand{position:absolute;left:139px;top:37px;width:186px;height:104px;background:var(--darker);border:1px solid #3c3c3c;display:flex;align-items:center;justify-content:center;text-align:center;font-size:24px;line-height:28px;color:var(--red)}
.footer-col h4{position:absolute;font-size:10px;font-weight:600;color:#fff}
.footer-links{position:absolute;list-style:none;font-size:7.5px;line-height:13.3px}
.footer-links svg{vertical-align:-1px;margin-right:6px}
.social-icon{display:inline-block;width:10px;height:10px;margin-right:9px;vertical-align:-1px}
.bottom-bar{position:absolute;left:0;top:1180px;width:834px;height:20px;background:#141414;color:#ccc;font-size:7px;line-height:20px;padding-left:139px}
</style>
</head>
<body>

<header class="site-header">
  <div class="brand">Larkspur Homes</div>
  <div class="header-contact">
    <div><svg width="7" height="7" viewBox="0 0 10 10"><path d="M2 0l2 2.5-1 1.5c.8 1.4 1.8 2.4 3 3l1.5-1L10 8 8.5 10C4 9.5.5 6 0 1.5z" fill="#bbb"/></svg>0700 4183265</div>
    <div><svg width="8" height="6" viewBox="0 0 10 7"><rect width="10" height="7" fill="#bbb"/><path d="M0 0l5 4 5-4" stroke="#2a2c2c" fill="none"/></svg>info@larkspur-homes.co.uk</div>
  </div>
</header>

<nav class="main-nav">
  <a class="active" style="left:138px;width:51px">Home</a>
  <a style="left:189px;width:130px">Sell Your Property Fast</a>
  <a style="left:319px;width:136px">Rent Your Property Fast</a>
  <a style="left:455px;width:99px">The 5 Easy Steps</a>
  <a style="left:554px;width:65px">About us</a>
  <a style="left:619px;width:77px">Contact us</a>
</nav>

<section class="hero">
  <div class="hero-photo" role="img" aria-label="Bright modern living room with white sofa, patterned cushions, black armchairs and a stone fireplace"></div>
  <h1 class="hero-title">Do you want to sell or rent out your<br>house quickly?</h1>
  <div class="hero-btn">Go</div>
  <div class="hero-dots"><span></span><span class="on"></span><span></span></div>
</section>

<h2 class="section-title intro-title">We are a local family run property business who specialize in</h2>
<div class="intro-figure" role="img" aria-label="Businessman in a dark suit holding a briefcase"></div>
<ul class="service-list">
  <li>• Buying properties quickly</li>
  <li>• Finding creative solutions to your property problems</li>
  <li>• Property rental management</li>
  <li>• Lettings to professional and student tenants</li>
  <li>• Guaranteed rent and management schemes for landlords</li>
  <li>• STOPPING repossessions</li>
  <li>• Motivated sellers</li>
  <li>• Chain fixing</li>
  <li>• Negative equity problems</li>
</ul>

<h2 class="section-title form-title">Contact Form</h2>
<form class="contact-form">
  <div class="field" style="top:12px">Name</div>
  <div class="field" style="top:38px">Email</div>
  <div class="field" style="top:63px">Phone number</div>
  <div class="field" style="top:89px">Property address</div>
  <div class="field" style="top:115px;height:42px">Message</div>
  <div class="send-btn">Send</div>
</form>

<section class="help">
  <h2 class="section-title help-title">Who can we help ?</h2>
  <div class="help-item" style="left:138px;top:76px"><b>1</b>How to stop repossession</div>
  <div class="help-item" style="left:138px;top:99px"><b>2</b>Divorce or separation</div>
  <div class="help-item" style="left:138px;top:121px"><b>3</b>Financial problems</div>
  <div class="help-item" style="left:138px;top:143px"><b>4</b>Don't like estate agents?</div>
  <div class="help-item" style="left:138px;top:165px"><b>5</b>Property needing work</div>
  <div class="help-item" style="left:344px;top:76px"><b>6</b>Retiring landlords</div>
  <div class="help-item" style="left:344px;top:99px"><b>7</b>Negative equity</div>
  <div class="help-item" style="left:344px;top:121px"><b>8</b>Opportunity not to be missed!!</div>
  <div class="help-item" style="left:344px;top:143px"><b>9</b>Guaranteed rent scheme</div>
  <div class="help-item" style="left:344px;top:165px"><b>10</b>Ill health</div>
  <div class="help-item" style="left:584px;top:76px"><b>11</b>Relocating</div>
  <div class="help-item" style="left:584px;top:99px"><b>12</b>Inherited property</div>
  <div class="help-item" style="left:584px;top:121px"><b>13</b>Chain Collapse</div>
  <div class="help-item" style="left:584px;top:143px"><b>14</b>Tenanted Property</div>
</section>

<h2 class="section-title partners-title">Partners</h2>
<div class="partner-badge" style="left:138px;width:96px;background:#d9d9d9;border-radius:4px" role="img" aria-label="Partner badge"></div>
<div class="partner-badge" style="left:268px;width:97px;background:var(--navy)" role="img" aria-label="Partner badge"></div>
<div class="partner-badge" style="left:403px;width:27px;background:#1b8fa8;border-radius:3px" role="img" aria-label="Partner badge"></div>
<div class="partner-badge" style="left:468px;width:96px;background:#d9d9d9;border-radius:4px" role="img" aria-label="Partner badge"></div>
<div class="partner-badge" style="left:599px;width:97px;background:var(--navy)" role="img" aria-label="Partner badge"></div>

<footer class="site-footer">
  <div class="footer-brand">Larkspur<br>Homes</div>
  <div class="footer-col">
    <h4 style="left:356px;top:40px">Sitemap</h4>
    <ul class="footer-links" style="left:356px;top:62px">
      <li>Home</li><li>Sell Your Property Fast</li><li>Rent Your Property Fast</li><li>The 5 Easy Steps</li><li>About us</li><li>Contact us</li>
    </ul>
  </div>
  <div class="footer-col">
    <h4 style="left:477px;top:40px">Contact us</h4>
    <ul class="footer-links" style="left:477px;top:62px;width:135px">
      <li>Lorem Ipsum is simply dummy text of the printing and typesetting</li>
      <li><svg width="8" height="6" viewBox="0 0 10 7"><rect width="10" height="7" fill="#999"/><path d="M0 0l5 4 5-4" stroke="#2a2c2c" fill="none"/></svg>info@larkspur-<br><span style="padding-left:16px">homes.co.uk</span></li>
      <li><svg width="8" height="8" viewBox="0 0 10 10"><path d="M2 0l2 2.5-1 1.5c.8 1.4 1.8 2.4 3 3l1.5-1L10 8 8.5 10C4 9.5.5 6 0 1.5z" fill="#999"/></svg>0700 4183265</li>
    </ul>
  </div>
  <div class="footer-col">
    <h4 style="left:639px;top:40px">Follow us</h4>
    <ul class="footer-links" style="left:640px;top:62px">
      <li><span class="social-icon" style="background:#3b5998"></span>Pagefeed</li>
      <li><span class="social-icon" style="background:#2ba9e1"></span>Chirpline</li>
      <li><span class="social-icon" style="background:#d9452f"></span>Orbitplus</li>
      <li><span class="social-icon" style="background:#1a7bb9"></span>Linkwork</li>
    </ul>
  </div>
</footer>
<div class="bottom-bar">2014 Larkspur Homes Limited. Reg No 5501726</div>

</body>
</html>
```